Halvik builders

Tarven Q480 year 2021 needs a full wrap. My companies name is Halvik Builders we are a high end landscape design build company. We specialize in pavers retaining walls, patio covers and decks.

```html
<!DOCTYPE html>
<html lang="en">
<head>
<meta charset="utf-8">
<title>Halvik Builders – Tarven Q480 Wrap</title>
<link rel="stylesheet" href="https://fonts.googleapis.com/css2?family=Cinzel:wght@700&family=Montserrat:wght@600;700;800&display=swap">
<style>
  :root {
    --teal: #0f3a44;
    --teal-deep: #0a2a31;
    --gold: #e9a71e;
    --white: #f3f4f4;
    --glass: #c9cfd2;
    --trim: #1b1b1b;
    --page: #ffffff;
  }
  html, body {
    margin: 0;
    width: 1200px;
    height: 1200px;
    overflow: hidden;
    background: var(--page);
  }
  .canvas {
    width: 1200px;
    height: 1200px;
    position: relative;
  }
  .wrap-variant {
    position: absolute;
    left: 100px;
    width: 1000px;
    height: 340px;
  }
  .wrap-variant--a { top: 170px; }
  .wrap-variant--b { top: 660px; }
  .body-white { fill: var(--white); }
  .panel-teal { fill: var(--teal); }
  .band-gold { fill: var(--gold); }
  .glass { fill: var(--glass); }
  .tyre { fill: var(--trim); }
  .rim { fill: #b9bec1; }
  .phone {
    font-family: "Montserrat", sans-serif;
    font-weight: 700;
    font-size: 22px;
    letter-spacing: 3px;
    fill: var(--gold);
  }
  .services {
    font-family: "Montserrat", sans-serif;
    font-weight: 600;
    font-size: 8px;
    fill: var(--white);
  }
  .brand-name {
    font-family: "Cinzel", serif;
    font-weight: 700;
    font-size: 28px;
    fill: var(--teal);
  }
  .tagline {
    font-family: "Montserrat", sans-serif;
    font-weight: 800;
    font-size: 12px;
    fill: var(--teal);
  }
  .web {
    font-family: "Montserrat", sans-serif;
    font-weight: 700;
    font-size: 13px;
    letter-spacing: 2px;
    fill: var(--teal);
  }
  .license {
    font-family: "Montserrat", sans-serif;
    font-weight: 700;
    font-size: 8.5px;
    fill: var(--teal);
  }
</style>
</head>
<body>
<main class="canvas">

  <svg class="wrap-variant wrap-variant--a" viewBox="0 0 1000 340" aria-label="Halvik Builders truck wrap, version with gold brand square">
    <defs>
      <clipPath id="truck-a">
        <path d="M20,100 L380,95 L392,22 Q396,8 420,8 L680,8 Q700,8 720,25 L790,100 L960,110 Q990,112 992,140 L995,255 L20,262 Z"/>
      </clipPath>
      <linearGradient id="bed-a" x1="0" y1="0" x2="1" y2="1">
        <stop offset="0" stop-color="#164650"/>
        <stop offset="1" stop-color="#0a2a31"/>
      </linearGradient>
    </defs>
    <g clip-path="url(#truck-a)">
      <rect class="body-white" x="0" y="0" width="1000" height="300"/>
      <rect x="0" y="80" width="390" height="200" fill="url(#bed-a)" role="img" aria-label="Stone wall texture in deep teal"/>
      <polygon class="panel-teal" points="520,0 1000,0 1000,112 760,112 700,40 520,40"/>
      <polygon class="band-gold" points="470,0 505,0 555,40 520,40"/>
      <polygon class="band-gold" points="520,118 1000,118 1000,128 540,128 520,140 480,140"/>
      <rect class="band-gold" x="395" y="196" width="605" height="30"/>
      <rect class="panel-teal" x="395" y="226" width="605" height="40"/>
    </g>
    <path class="glass" d="M410,24 Q412,18 420,18 L500,18 L505,100 L410,100 Z"/>
    <path class="glass" d="M520,18 L670,18 Q690,18 705,34 L760,100 L520,100 Z"/>
    <circle class="body-white" cx="210" cy="262" r="68"/>
    <circle class="body-white" cx="850" cy="262" r="68"/>
    <circle class="tyre" cx="210" cy="272" r="56"/>
    <circle class="rim" cx="210" cy="272" r="36"/>
    <circle class="tyre" cx="850" cy="272" r="56"/>
    <circle class="rim" cx="850" cy="272" r="36"/>

    <text class="phone" x="75" y="132">(206) 555-0148</text>
    <text class="services" x="44" y="152" textLength="248" lengthAdjust="spacingAndGlyphs">Paver Patios and Driveways ▪ Retaining Walls ▪ Decks &amp; Railings</text>
    <text class="services" x="44" y="166">Pools ▪ Outdoor Lighting ▪ Firepits and Fireplaces</text>
    <rect class="band-gold" x="300" y="112" width="95" height="95"/>
    <text class="brand-name" x="402" y="170">HALVIK BUILDERS</text>
    <text class="tagline" x="436" y="188">OUTDOOR LIVING SPACES</text>
    <text class="web" x="440" y="216">halvikbuilders.com</text>
    <text class="license" x="830" y="140">License # HALVIBL825QB</text>
  </svg>

  <svg class="wrap-variant wrap-variant--b" viewBox="0 0 1000 340" aria-label="Halvik Builders truck wrap, version with teal brand square">
    <defs>
      <clipPath id="truck-b">
        <path d="M20,100 L380,95 L392,22 Q396,8 420,8 L680,8 Q700,8 720,25 L790,100 L960,110 Q990,112 992,140 L995,255 L20,262 Z"/>
      </clipPath>
      <linearGradient id="bed-b" x1="0" y1="0" x2="1" y2="1">
        <stop offset="0" stop-color="#164650"/>
        <stop offset="1" stop-color="#0a2a31"/>
      </linearGradient>
    </defs>
    <g clip-path="url(#truck-b)">
      <rect class="body-white" x="0" y="0" width="1000" height="300"/>
      <rect x="0" y="80" width="390" height="200" fill="url(#bed-b)" role="img" aria-label="Stone wall texture in deep teal"/>
      <polygon class="panel-teal" points="520,0 1000,0 1000,112 760,112 700,40 520,40"/>
      <polygon class="band-gold" points="470,0 505,0 555,40 520,40"/>
      <polygon class="band-gold" points="520,118 1000,118 1000,128 540,128 520,140 480,140"/>
      <rect class="band-gold" x="395" y="196" width="605" height="30"/>
      <rect class="panel-teal" x="395" y="226" width="605" height="40"/>
    </g>
    <path class="glass" d="M410,24 Q412,18 420,18 L500,18 L505,100 L410,100 Z"/>
    <path class="glass" d="M520,18 L670,18 Q690,18 705,34 L760,100 L520,100 Z"/>
    <circle class="body-white" cx="210" cy="262" r="68"/>
    <circle class="body-white" cx="850" cy="262" r="68"/>
    <circle class="tyre" cx="210" cy="272" r="56"/>
    <circle class="rim" cx="210" cy="272" r="36"/>
    <circle class="tyre" cx="850" cy="272" r="56"/>
    <circle class="rim" cx="850" cy="272" r="36"/>

    <text class="phone" x="75" y="132">(206) 555-0148</text>
    <text class="services" x="44" y="152" textLength="248" lengthAdjust="spacingAndGlyphs">Paver Patios and Driveways ▪ Retaining Walls ▪ Decks &amp; Railings</text>
    <text class="services" x="44" y="166">Pools ▪ Outdoor Lighting ▪ Firepits and Fireplaces</text>
    <rect class="panel-teal" x="300" y="112" width="95" height="95"/>
    <text class="brand-name" x="402" y="170">HALVIK BUILDERS</text>
    <text class="tagline" x="436" y="188">OUTDOOR LIVING SPACES</text>
    <text class="web" x="440" y="216">halvikbuilders.com</text>
    <text class="license" x="830" y="140">License # HALVIBL825QB</text>
  </svg>

</main>
</body>
</html>
```